Ridgeline Athletic Academy needs a creative web design

Ridgeline Athletic Academy (RAA) is a new sports company in North Texas, We offer basketball, Volleyball and sports performance training. We are a unique company that integrates sports performance with a specific sport to build a well rounded athlete who can compete at the next level. We would like to see designs use our team colors Blue, lime green and grey. The final design will communicate and fundamentally based program that is ahead of the times in training its athletes.

Target Market(s)

Youth athletes, boys and girls wanting to play volleyball and/or Basketball either at the recreational or tournament level.

Coding

Number of Pages Required

5+ page

Font styles to use
Sans Serif

Requirements
Must have
• Pics rotating every 3-5 secs, Limited white space. Links to Facebook, Twitter and Instagram. Message board, In the news section, calendar or schedule. Will provide the links. Registration link. Will provide link. Payment section. Will provide the details of the banking service.
• Will be supplying the action pics and pics of the coaches when they are done. Please just put placeholder pics in there for now.
Nice to have
• I have included a layout but please do not adhere to this this. Feel free to come up with your own ideas on how you feel the information should be presented.

```html
<!DOCTYPE html>
<html lang="en">
<head>
<meta charset="utf-8">
<title>Ridgeline Athletic Academy – Registration</title>
<link href="https://fonts.googleapis.com/css2?family=Open+Sans:wght@400;600;700;800&display=swap" rel="stylesheet">
<style>
:root{
  --navy:#0f2a4a;
  --blue:#1d5fa8;
  --lime:#8cc63f;
  --grey:#8a8f96;
  --grey-light:#e6e8eb;
  --dark:#1b1e22;
  --text:#3a3f45;
  --white:#ffffff;
}
*{box-sizing:border-box;margin:0;padding:0}
html,body{width:667px;height:1200px;overflow:hidden}
body{font-family:"Open Sans",Arial,sans-serif;color:var(--text);background:var(--white);font-size:6.5px;line-height:1.45;position:relative}
.site-header{height:58px;background:var(--dark);display:flex;align-items:center;justify-content:space-between;padding:0 22px}
.phone{display:flex;align-items:center;gap:6px;color:var(--white);font-size:9px;font-weight:600}
.brand{display:flex;align-items:center;gap:6px;color:var(--white);font-weight:800;font-size:17px;letter-spacing:1px}
.brand .dot{width:14px;height:14px;border-radius:50%;background:var(--lime)}
.social{display:flex;gap:6px}
.social span{width:20px;height:20px;border-radius:50%;background:var(--blue)}
.main-nav{height:22px;background:var(--navy);display:flex;align-items:stretch;padding:0 16px}
.main-nav a{color:var(--white);text-decoration:none;font-size:6.5px;font-weight:700;padding:0 9px;display:flex;align-items:center}
.main-nav a.active{background:var(--lime)}
.content{display:flex;gap:18px;padding:14px 16px 0}
.primary{width:410px}
.sidebar{width:207px}
h2{font-size:9px;font-weight:800;color:var(--navy);text-transform:uppercase;margin-bottom:5px}
h2 .link{font-weight:400;font-size:6px;color:var(--blue);text-transform:none;margin-left:6px}
h3{font-size:8px;font-weight:800;color:var(--navy);text-transform:uppercase;margin:10px 0 4px}
p{margin-bottom:5px}
.hl{color:var(--lime);font-weight:700}
.cta{color:var(--blue);font-weight:700;text-decoration:underline}
.rule{border-top:1px solid var(--grey-light);margin:8px 0}
.pricing{background:var(--blue);margin:8px -16px 0 -16px;padding:10px 16px 12px;width:444px}
.pricing h2{color:var(--white)}
.price-grid{display:grid;grid-template-columns:1fr 1fr;gap:8px}
.price-card{display:flex;height:42px;color:var(--white)}
.price-card .label{flex:1;padding:5px 7px;font-size:6px;background:var(--grey)}
.price-card .amount{width:78px;background:var(--white);color:var(--navy);font-size:13px;font-weight:800;display:flex;align-items:center;justify-content:center}
.price-card .amount small{font-size:6px;font-weight:400;margin-left:2px}
.price-card.featured .label{background:var(--lime)}
.location{background:var(--dark);margin:8px -16px 0;width:444px;height:100px;display:flex}
.map{width:220px;background:linear-gradient(135deg,#4b5158,#2c3035)}
.location .info{flex:1;padding:20px 12px;color:#cfd3d8;font-size:6px}
.location h2{color:var(--white)}
.coach{margin-bottom:26px}
.coach .photo{height:115px;border-radius:2px}
.coach h4{font-size:8.5px;font-weight:800;color:var(--navy);text-transform:uppercase;margin:5px 0 3px}
.site-footer{position:absolute;left:0;top:1112px;width:667px;height:88px;background:var(--dark);color:#b9bec4;text-align:center;padding-top:14px}
.site-footer .social{justify-content:center;margin-bottom:10px}
.footer-links{font-size:6.5px;margin-bottom:6px}
.footer-links span{margin:0 4px}
.copy{font-size:6px}
</style>
</head>
<body>
<header class="site-header">
  <div class="phone">
    <svg width="14" height="14" viewBox="0 0 24 24"><circle cx="12" cy="12" r="12" fill="#1d5fa8"/><path d="M8 6l2 0 1 3-1.5 1a7 7 0 0 0 4 4l1-1.5 3 1v2a1 1 0 0 1-1 1A10 10 0 0 1 7 7a1 1 0 0 1 1-1z" fill="#fff"/></svg>
    +1 555 014 2290
  </div>
  <div class="brand"><span class="dot"></span>RAA VOLLEYBALL</div>
  <div class="social"><span></span><span></span><span></span></div>
</header>
<nav class="main-nav">
  <a>HOME</a><a>ABOUT</a><a>BASKETBALL</a><a>VOLLEYBALL</a><a>PERFORMANCE</a><a>COACHES</a><a>CALENDAR</a><a class="active">REGISTRATION</a><a>NEWS</a><a>CONTACT</a>
</nav>

<div class="content">
  <main class="primary">
    <h2>Registration <span class="link">http://register.example.com/raa/volleyball/2016-spring-skills</span></h2>
    <h3>Skills</h3>
    <p><strong>Monday/Wednesdays</strong></p>
    <p><span class="hl">5-7pm (Advanced Hitters)</span> – These sessions are designed for the player who is new to the game or is capable of playing at the recreational level. The players are instructed on the core fundamentals and get many repetitions and feedback throughout the skills session.</p>
    <p><span class="hl">7-8pm (Sports Performance/Athletic Features)</span> – the sports performance sessions are designed to improve the players athleticism through repetition, agility, strength, flexibility and conditioning exercises.</p>
    <p><span class="hl">8-9pm (Advanced Hitters)</span> – these sessions are designed for the advanced players who are capable of playing at the tournament level or looking to play at tournament level. During these sessions the players are focused on fine-tuning the core fundamental base, implementing advanced skills and game-like drills prior to tryouts to make the club team.</p>
    <div class="rule"></div>
    <h3>Teams</h3>
    <p>All RAA volleyball clubs are for all levels of age groups 12U through 18U girls. Volleyball is not only a female sport, but a male sport as well. We are looking forward to developing our boys program to expand in the Dallas area with the help of the Northline Court Club. We have a Level and a 50-player roster for Fall 2016 seasons.</p>
    <p><strong>Recreational Teams</strong></p>
    <p>This season's teams play in the Summit Hall and Prairie Rec League. The teams are formed based on ability and then are placed in the correct division in the local leagues so that the players can maximize the experience. Every team plays at least 8 games. RAA teams also play in the RAA Fall and Spring Bash tournament. The teams play 8 game sessions with at least a 9 day break between seasons. You can find more details on the team on the <span class="cta">Summit Hall</span> and <span class="cta">Prairie Rec League</span> websites.</p>
    <p>Uniform – Jersey and Spandex</p>
    <p class="cta">Click Here To see Team Page</p>
    <p><strong>Tournament Teams</strong></p>
    <p>RAA offers tournament teams from the 12U grade that will play in local and regional events. The tournament season goes from December to June and will be posted in the Dallas/Fort Worth area. Teams will play on average 6 weekends a month. RAA is affiliated with the Northline Court Club, which is a part of the Lone Plains Volleyball Region.</p>
    <p>Uniform – Jersey, spandex, knee pads, socks, shoes, backpack</p>
    <p class="cta">Click Here To see Team Page</p>

    <section class="pricing">
      <h2>Pricing</h2>
      <div class="price-grid">
        <div class="price-card featured"><div class="label">Skills Only – Monday Night 4 sessions</div><div class="amount">$ 100<small>/month</small></div></div>
        <div class="price-card"><div class="label">Skills Only – Wednesday Night 4 sessions</div><div class="amount">$ 135<small>/month</small></div></div>
        <div class="price-card"><div class="label">Punch Card – 4 sessions of skills and/or sports performance</div><div class="amount">$ 115<small>/month</small></div></div>
        <div class="price-card"><div class="label">Team + Skills + Sports Performance</div><div class="amount">$ 80<small>/month</small></div></div>
      </div>
    </section>

    <h2 style="margin-top:12px">Registration <span class="link">http://register.example.com/raa/volleyball/2016-spring-teams</span></h2>

    <section class="location">
      <div class="map" role="img" aria-label="Map showing the academy's training locations"></div>
      <div class="info">
        <h2>Location</h2>
        <p>Volleyball: Northline Court Club, 1510 Oak Row, Cedar Falls, TX 75090, United States</p>
        <p>Basketball: Northline Court Club, 1510 Oak Row, Cedar Falls, TX 75090, United States</p>
      </div>
    </section>

    <h2 style="margin-top:12px">Times and Dates of Sessions</h2>
    <p>RAA Volleyball operates on Monday and Wednesday evenings from 5-9pm at Northline Court Club in Cedar Falls, Texas.</p>
    <p>Our location changes to Northline Court Club for the month of December. Please check the changes on your calendar so you do not miss out on a night of progress.</p>
  </main>

  <aside class="sidebar">
    <div class="coach" style="margin-top:40px">
      <div class="photo" role="img" aria-label="Portrait photo of coach Dana Whitfield" style="background:linear-gradient(160deg,#c9b39a,#6d5a48)"></div>
      <h4>Dana Whitfield</h4>
      <p>Dana grew up in Cedar Falls where she attended Ridgeline High School and was part of the 2004 State Championship volleyball team as a freshman. Her drive and passion led her to coach.</p>
      <p class="cta">Click Here to Read More</p>
    </div>
    <div class="coach">
      <div class="photo" role="img" aria-label="Portrait photo of coach Lena Marchetti" style="background:linear-gradient(160deg,#a7b4c2,#3e4c5c)"></div>
      <h4>Lena Marchetti</h4>
      <p>Lena attended Westbrook High School during some of their most successful consecutive volleyball seasons. Her strong playing ability landed her a full scholarship to play in college.</p>
      <p class="cta">Click Here to Read More</p>
    </div>
    <div class="coach">
      <div class="photo" role="img" aria-label="Portrait photo of coach Corinne Hale" style="background:linear-gradient(160deg,#d8c2a4,#7a6550)"></div>
      <h4>Corinne Hale</h4>
      <p>Corinne grew up in the region. Those visits she attended Lake Ives High School and earned a Bachelor of Science Degree in Early Childhood Development, and a Master's Degree in Education.</p>
      <p class="cta">Click Here to Read More</p>
    </div>
    <div class="coach">
      <div class="photo" role="img" aria-label="Portrait photo of coach Maya Lindqvist" style="background:linear-gradient(160deg,#cbbfae,#5e5548)"></div>
      <h4>Maya Lindqvist</h4>
      <p>Maya is a native of Lafayette, Indiana and moved to Cedar Falls in 2015 where she is a sophomore at Ridgeline High School. She played competitive volleyball, soccer and more.</p>
      <p class="cta">Click Here to Read More</p>
    </div>
  </aside>
</div>

<footer class="site-footer">
  <div class="social"><span></span><span></span><span></span></div>
  <div class="footer-links"><span>Home</span>|<span>About</span>|<span>Basketball</span>|<span>Volleyball</span>|<span>Performance</span>|<span>Coaches</span>|<span>Calendar</span>|<span>Registration</span>|<span>News</span>|<span>Contact</span></div>
  <div class="copy">© Copyright 2016 RAA. All Rights Reserved</div>
</footer>
</body>
</html>
```